Business Card Design for Occupational Medicine Start Up Company

We need to design a professional business card. We are a healthcare company providing occupational medicine services to blue collar industries. We are professional, efficient and high quality service providers.

Target Market(s)

Blue Collar Industry: Shipbuilding, Ports, Trucking Companies; The Executives and Safety Officers for these companies

Industry/Entity Type

Healthcare

Contact Information for Business Card

Logo, Name, Title, Email, Phone

Other font styles liked:
• Please match our Brand Guide

Requirements
Must have
• Our Company Colors and Logo

```html
<!DOCTYPE html>
<html lang="en">
<head>
<meta charset="UTF-8">
<title>Harborline Clinics – Business Card</title>
<link rel="stylesheet" href="https://fonts.googleapis.com/css2?family=Montserrat:wght@400;500;600;700&display=swap">
<style>
  :root {
    --navy: #262c83;
    --sky: #1e9bd7;
    --paper: #ffffff;
    --backdrop: #e3e6e7;
  }
  * { box-sizing: border-box; margin: 0; padding: 0; }
  html, body {
    width: 1200px;
    height: 800px;
    overflow: hidden;
    background: var(--backdrop);
    font-family: "Montserrat", sans-serif;
  }
  .canvas {
    position: relative;
    width: 1200px;
    height: 800px;
  }
  .card {
    position: absolute;
    width: 441px;
    height: 276px;
  }
  /* Front side */
  .card--front {
    left: 193px;
    top: 101px;
    background: var(--paper);
  }
  .brand {
    position: absolute;
    display: flex;
    align-items: center;
    gap: 8px;
  }
  .brand__mark {
    border-radius: 50%;
    flex: none;
  }
  .brand__name {
    font-weight: 600;
    text-transform: uppercase;
    line-height: 1.1;
  }
  .card--front .brand {
    left: 19px;
    top: 24px;
  }
  .card--front .brand__mark {
    width: 28px;
    height: 28px;
    background: var(--navy);
  }
  .card--front .brand__name {
    color: var(--navy);
    font-size: 10px;
    letter-spacing: 0.4px;
  }
  .divider {
    position: absolute;
    left: 245px;
    width: 3px;
    background: var(--navy);
  }
  .divider--top { top: 0; height: 98px; border-radius: 0 0 2px 2px; }
  .divider--bottom { bottom: 0; height: 44px; border-radius: 2px 2px 0 0; }
  .holder {
    position: absolute;
    left: 19px;
    top: 139px;
  }
  .holder__name {
    color: var(--navy);
    font-size: 17px;
    font-weight: 700;
    letter-spacing: 0.3px;
  }
  .holder__role {
    margin-top: 4px;
    color: var(--sky);
    font-size: 12px;
    font-weight: 400;
    letter-spacing: 0.3px;
  }
  .contacts {
    position: absolute;
    left: 245px;
    top: 118px;
    list-style: none;
  }
  .contacts__item {
    display: flex;
    align-items: center;
    gap: 6px;
    height: 13px;
    margin-bottom: 11px;
    color: var(--navy);
    font-size: 8.5px;
    font-weight: 500;
  }
  .contacts__icon {
    width: 13px;
    height: 13px;
    border-radius: 2px;
    background: var(--navy);
    display: flex;
    align-items: center;
    justify-content: center;
    flex: none;
  }
  .contacts__icon svg { width: 8px; height: 8px; }
  /* Back side */
  .card--back {
    left: 567px;
    top: 423px;
    background: var(--navy);
  }
  .card--back .brand {
    left: 0;
    right: 0;
    top: 0;
    bottom: 0;
    justify-content: center;
    gap: 16px;
  }
  .card--back .brand__mark {
    width: 62px;
    height: 62px;
    background: var(--paper);
  }
  .card--back .brand__name {
    color: var(--paper);
    font-size: 21px;
    letter-spacing: 0.6px;
  }
</style>
</head>
<body>
<main class="canvas">

  <section class="card card--front" aria-label="Business card front">
    <div class="brand">
      <span class="brand__mark"></span>
      <span class="brand__name">Harborline<br>Clinics</span>
    </div>

    <span class="divider divider--top"></span>
    <span class="divider divider--bottom"></span>

    <div class="holder">
      <p class="holder__name">NAME SURNAME</p>
      <p class="holder__role">POSITION</p>
    </div>

    <ul class="contacts">
      <li class="contacts__item">
        <span class="contacts__icon">
          <svg viewBox="0 0 10 10"><path d="M2 1.2 3.4 1l.8 2-1 .7a5 5 0 0 0 2.1 2.1l.7-1 2 .8-.2 1.4c-3.6.4-6.2-2.2-5.8-5.8Z" fill="#fff"/></svg>
        </span>
        +012 34567890
      </li>
      <li class="contacts__item">
        <span class="contacts__icon">
          <svg viewBox="0 0 10 10"><rect x="1" y="2.2" width="8" height="5.6" fill="none" stroke="#fff" stroke-width="1"/><path d="M1 2.4 5 5.6 9 2.4" fill="none" stroke="#fff" stroke-width="1"/></svg>
        </span>
        email@yourcompany.com
      </li>
      <li class="contacts__item">
        <span class="contacts__icon">
          <svg viewBox="0 0 10 10"><path d="M5 9.4S2 6 2 4a3 3 0 0 1 6 0c0 2-3 5.4-3 5.4Z" fill="#fff"/><circle cx="5" cy="4" r="1.1" fill="#262c83"/></svg>
        </span>
        Company street
      </li>
      <li class="contacts__item">
        <span class="contacts__icon">
          <svg viewBox="0 0 10 10" fill="none" stroke="#fff" stroke-width="0.8"><circle cx="5" cy="5" r="3.8"/><ellipse cx="5" cy="5" rx="1.6" ry="3.8"/><path d="M1.2 5h7.6M1.8 3h6.4M1.8 7h6.4"/></svg>
        </span>
        www.companywebsite.com
      </li>
    </ul>
  </section>

  <section class="card card--back" aria-label="Business card back">
    <div class="brand">
      <span class="brand__mark"></span>
      <span class="brand__name">Harborline<br>Clinics</span>
    </div>
  </section>

</main>
</body>
</html>
```